Business Card

We need some ideas for corporate business cards. I'm interested in a double sided card, with one side featuring our corporate logo, the other side with employee information.

Corporate colors, logo etc. available at www.brivalo.com

Industry/Entity Type

Business

Requirements
Must have
• The "Brivalo" logo with stylized "O"

Nice to have
• Preferred font is calibri

```html
<!DOCTYPE html>
<html lang="en">
<head>
<meta charset="utf-8">
<title>Brivalo Business Card</title>
<link rel="stylesheet" href="https://fonts.googleapis.com/css2?family=Carlito:wght@400;700&display=swap">
<style>
  :root {
    --brand-blue: #4a62a0;
    --brand-blue-dark: #3c5390;
    --card-white: #f6f6f7;
    --card-grey: #e9eaeb;
    --panel-white: #f8f8f8;
    --ink: #1f1f22;
    --stage: #d6d7d9;
    --photo-light: #eef0f6;
    --photo-mid: #b9c2dc;
    --photo-lilac: #d7cbe0;
  }
  * { box-sizing: border-box; margin: 0; padding: 0; }
  html, body {
    width: 1200px; height: 900px; overflow: hidden;
    background: var(--stage);
    font-family: "Carlito", "Calibri", sans-serif;
  }
  .sheet {
    width: 1200px; height: 900px;
    display: flex; flex-direction: column; align-items: center; justify-content: center;
    gap: 50px;
  }
  .card {
    position: relative;
    width: 620px; height: 360px;
    border-radius: 18px;
    overflow: hidden;
    box-shadow: 0 4px 14px rgba(0,0,0,.15);
  }
  .card svg.card-art { position: absolute; inset: 0; }

  /* Front side */
  .card-front { background: var(--card-white); }
  .front-brand {
    position: absolute; right: 42px; top: 30px;
    text-align: right; color: #fff;
  }
  .front-brand .wordmark {
    font-weight: 700; font-size: 58px; letter-spacing: 5px; line-height: 1;
  }
  .front-brand .web {
    margin-top: 6px; font-size: 13px; letter-spacing: 4px;
  }

  /* Back side */
  .card-back { background: var(--card-grey); color: var(--ink); }
  .back-logo {
    position: absolute; left: 40px; top: 128px;
    font-weight: 700; font-size: 46px; letter-spacing: 4px;
    color: var(--brand-blue); line-height: 1;
  }
  .name-panel {
    position: absolute; left: 330px; top: 26px; width: 262px; height: 70px;
    background: var(--panel-white); padding: 14px 0 0 18px;
  }
  .name-panel .person { font-weight: 700; font-size: 19px; letter-spacing: .5px; }
  .name-panel .role { font-size: 15px; color: var(--brand-blue); }
  .contact-panel {
    position: absolute; left: 326px; top: 168px; width: 236px; height: 116px;
    background: var(--panel-white); padding: 14px 0 0 20px;
    font-size: 15px; line-height: 21px;
  }
  .contact-panel .label, .contact-panel .accent { color: var(--brand-blue); }
  .address {
    position: absolute; left: 40px; top: 222px;
    font-size: 15px; line-height: 20px;
  }
</style>
</head>
<body>
<main class="sheet">

  <section class="card card-front" aria-label="Card front">
    <svg class="card-art" width="620" height="360" viewBox="0 0 620 360">
      <defs>
        <linearGradient id="photoTone" x1="0" y1="1" x2="1" y2="0">
          <stop offset="0" stop-color="var(--photo-mid)"/>
          <stop offset=".45" stop-color="var(--photo-light)"/>
          <stop offset=".75" stop-color="var(--photo-lilac)"/>
          <stop offset="1" stop-color="var(--photo-mid)"/>
        </linearGradient>
      </defs>
      <rect class="top-band" x="0" y="0" width="620" height="140" fill="var(--brand-blue)"/>
      <path class="white-strip" d="M0 150 L620 118 L620 140 L0 140 Z" fill="var(--card-white)"/>
      <path class="photo-area" role="img" aria-label="Photo of a glass and steel atrium roof seen from below"
            d="M0 162 L620 130 L620 262 Q320 292 40 330 Q0 336 0 318 Z" fill="url(#photoTone)"/>
    </svg>
    <div class="front-brand">
      <div class="wordmark">BRIVALO</div>
      <div class="web">www.brivalo.com</div>
    </div>
  </section>

  <section class="card card-back" aria-label="Card back">
    <svg class="card-art" width="620" height="360" viewBox="0 0 620 360">
      <path class="bottom-band" d="M0 336 L620 312 L620 360 L0 360 Z" fill="var(--brand-blue)"/>
    </svg>
    <div class="back-logo">BRIVALO</div>
    <div class="name-panel">
      <div class="person">DANIEL MORROW</div>
      <div class="role">Lead Manager</div>
    </div>
    <div class="contact-panel">
      <div><span class="label">Tel:</span> +353 1 555 0142</div>
      <div><span class="label">Fax:</span> +353 1 555 0198</div>
      <div><span class="accent">info</span>@brivalo.com</div>
      <div>www.<span class="accent">brivalo</span>.com</div>
    </div>
    <address class="address" style="font-style:normal">
      14 Harbour Row,<br>
      Millbrook Business Park, Dublin 12<br>
      Dublin, DB<br>
      Ireland
    </address>
  </section>

</main>
</body>
</html>
```